6x9 Postcard "401k Rollover" to market Individuals to transfer their retirement savings to our firm

Formats: .jpg, .png, .psd, .ai
Dimensions: See uploaded documents

We need a postcard to encourage people 45-65 years olds to transfer their retirement plan assets to our financial advising firm. We have uploaded an example we've been working please feel free to use your artistic license to make it look good images etc. You do not need to copy it word for word, we welcome creativity.

Suggested Wording:

We make it easy to rollover your old 401k

Spread the word! If you or someone you know has a 401k with a former employer or has reached age 59 1/2, consider a 401k rollover

The Marlowe Financial team can help rollover your old 401k

Advantages of a rollover: control over your accounts, more investment options, professional investment management, consolidate and simplify your accounts, guaranteed lifetime income options, help from a team of dedicated advisors

Make the most of your old 401k with a new Rollover IRA, speak with a trusted advisor today, (661)555-0142

If the QWM logo is used it MUST be used with the name "Gerald Pruitt" near it to clearly associate the two. if the words are used they Must be after his name and in all caps like this "Gerald Pruitt, ACCREDITED WEALTH STEWARD TM" [super script TM]. These are rules of the QWM trade mark.

Target Market(s)

Age 45 to 65 with sizable assets in 401k retirement plans

Industry/Entity Type

Investment Advisory

Font styles to use
Serif
Sans Serif
Decorative
Script

Colors

Designer to choose colors to be used in the design.

Requirements
Must have
• The post card MUST contain the following text at least 8pt font:
• Securities offered through Ember Ridge Securities, L.P. Member - NEVOC/TALQ | 4875 North Elm Rd, Ste 120, Lancaster, CA 93536 | 800.555.0173 | CA Ins. Lic. #0K48391, #0713948, #0K52806, #0619427
• Must have website and phone number:
• www.geraldpruittadvisory.example
• (661) 555-0142
Nice to have
• We would like the design to convey: Trust, Safety, Growth, Wealth, Planning, Strength, Stable, Peace of Mind, Time, Classic, Legacy

```html
<!DOCTYPE html>
<html lang="en">
<head>
<meta charset="utf-8">
<title>401k Rollover Postcard – Gerald Pruitt</title>
<link href="https://fonts.googleapis.com/css2?family=Montserrat:wght@500;600;700;800&family=Oswald:wght@400;500&family=Roboto+Condensed:ital,wght@0,400;0,700;1,400&display=swap" rel="stylesheet">
<style>
  :root{
    --navy:#0f2a5c;
    --royal:#1b3fa6;
    --sky:#6fc3ee;
    --ink:#1a1a1a;
    --paper:#ffffff;
    --stage:#d9dadc;
    --sand:#d8d2ca;
  }
  *{box-sizing:border-box;margin:0;padding:0}
  html,body{width:1200px;height:1000px;overflow:hidden;background:var(--stage)}
  .postcard{position:absolute;top:313px;width:560px;height:373px;overflow:hidden;box-shadow:0 3px 10px rgba(0,0,0,.35)}
  .postcard--front{left:30px}
  .postcard--back{left:610px;background:linear-gradient(170deg,#fff 0%,#fbfaf9 35%,#e4e0dc 70%,var(--sand) 100%)}

  /* front */
  .hero-photo{position:absolute;inset:0;background:
     radial-gradient(ellipse at 30% 60%,#f1e6da 0%,rgba(241,230,218,0) 45%),
     linear-gradient(160deg,#b88f2c 0%,#cfae4c 25%,#a9b55a 55%,#8fa64a 80%,#c9c08a 100%)}
  .headline-banner{position:absolute;left:340px;top:0;width:192px;height:285px;background:linear-gradient(90deg,#f2f2f2,#fff 40%,#eaeaea);
     clip-path:polygon(0 0,100% 0,100% 86%,0 100%);padding:18px 14px 0 10px;text-align:right;font-family:"Montserrat",sans-serif;color:var(--ink)}
  .banner-shadow{position:absolute;left:346px;top:0;width:192px;height:290px;background:rgba(0,0,0,.35);filter:blur(5px);clip-path:polygon(0 0,100% 0,100% 86%,0 100%)}
  .headline-line{font-size:21px;font-weight:600;line-height:25px;letter-spacing:.2px}
  .headline-line--accent{color:var(--royal)}
  .headline-number{font-size:46px;font-weight:800;line-height:48px;color:var(--royal);letter-spacing:.5px}
  .advisor-name{margin-top:16px;text-align:center;font-size:11px;font-weight:600;letter-spacing:2.2px}
  .designation{margin-top:7px;display:flex;align-items:center;justify-content:center;gap:6px;text-align:left}
  .designation-mark{font-size:16px;font-weight:700;letter-spacing:1px}
  .designation-words{font-size:7px;font-weight:600;line-height:9px;letter-spacing:1px}
  .designation-words sup{font-size:5px}
  .contact-stripe{position:absolute;left:0;right:0;top:318px;height:5px;background:var(--sky)}
  .contact-band{position:absolute;left:0;right:0;top:323px;bottom:0;background:var(--navy);display:flex;align-items:center;justify-content:center;gap:8px;font-family:"Oswald",sans-serif;font-size:17px}
  .contact-label{color:var(--sky);font-weight:400;letter-spacing:.3px}
  .contact-url{color:#fff;font-family:"Roboto Condensed",sans-serif;font-size:18px}

  /* back */
  .back-header{position:absolute;left:24px;top:24px;display:flex;align-items:center;gap:6px}
  .spread-tag{background:var(--navy);color:#8fd3f4;font-family:"Oswald",sans-serif;font-size:25px;line-height:32px;padding:0 6px;letter-spacing:.3px}
  .spread-copy{font-family:"Roboto Condensed",sans-serif;font-size:10.5px;line-height:13px;color:var(--ink);text-transform:uppercase}
  .team-callout{position:absolute;left:85px;top:72px;width:393px;border:1.5px solid var(--navy);text-align:center;font-family:"Roboto Condensed",sans-serif;font-size:11.5px;line-height:17px;color:var(--ink);background:#fff}
  .advantages{position:absolute;left:40px;top:125px;width:245px;height:130px;border:1.5px solid var(--navy)}
  .advantages-title{position:absolute;left:22px;top:-11px;background:#fff;padding:0 6px;font-family:"Oswald",sans-serif;font-size:16px;color:var(--navy);line-height:20px}
  .advantages-list{list-style:none;margin:14px 0 0 4px;font-family:"Roboto Condensed",sans-serif;font-style:italic;font-size:13px;line-height:17.5px;color:var(--ink)}
  .advantages-list li{display:flex;align-items:center;gap:5px}
  .tick{width:11px;height:11px;flex:none}
  .cta{position:absolute;left:40px;top:262px;width:245px;text-align:center;font-family:"Roboto Condensed",sans-serif;font-size:11px;line-height:13px;color:var(--ink)}
  .cta-phone{display:flex;align-items:center;justify-content:center;gap:4px;font-family:"Montserrat",sans-serif;font-weight:700;font-size:17px;color:var(--navy);margin-top:2px}
  .disclosure{position:absolute;left:24px;top:318px;width:185px;font-family:"Roboto Condensed",sans-serif;font-size:6px;line-height:7.5px;color:var(--ink)}
  .mailing-area{position:absolute;background:#fff}
  .mailing-area--upper{left:318px;top:187px;right:0;height:128px}
  .mailing-area--lower{left:186px;top:315px;right:0;bottom:0}
</style>
</head>
<body>

<section class="postcard postcard--front">
  <div class="hero-photo" role="img" aria-label="Photo of a smiling retired couple embracing outdoors in an autumn park"></div>
  <div class="banner-shadow"></div>
  <div class="headline-banner">
    <div class="headline-line">WE MAKE IT</div>
    <div class="headline-line">EASY TO</div>
    <div class="headline-line headline-line--accent">ROLLOVER</div>
    <div class="headline-line">YOUR OLD</div>
    <div class="headline-number">401K</div>
    <div class="advisor-name">GERALD PRUITT</div>
    <div class="designation">
      <span class="designation-mark">QWM</span>
      <span class="designation-words">ACCREDITED<sup>™</sup><br>WEALTH<br>STEWARD</span>
    </div>
  </div>
  <div class="contact-stripe"></div>
  <div class="contact-band">
    <span class="contact-label">CONTACT US TODAY:</span>
    <span class="contact-url">www.geraldpruittadvisory.example</span>
  </div>
</section>

<section class="postcard postcard--back">
  <div class="back-header">
    <div class="spread-tag">SPREAD THE WORD!</div>
    <p class="spread-copy">If you or someone you know has a 401k with a former<br>employer “or” has reached age 59 1/2, consider a 401k rollover</p>
  </div>
  <div class="team-callout">THE GERALD PRUITT FINANCIAL TEAM CAN HELP ROLLOVER YOUR OLD 401K</div>

  <div class="mailing-area mailing-area--upper"></div>
  <div class="mailing-area mailing-area--lower"></div>

  <div class="advantages">
    <h2 class="advantages-title">ADVANTAGES OF A ROLLOVER</h2>
    <ul class="advantages-list">
      <li><svg class="tick" viewBox="0 0 12 12"><path d="M1 6.5l3 3L11 2" fill="none" stroke="#0f2a5c" stroke-width="2"/></svg>Control over your accounts</li>
      <li><svg class="tick" viewBox="0 0 12 12"><path d="M1 6.5l3 3L11 2" fill="none" stroke="#0f2a5c" stroke-width="2"/></svg>More investment options</li>
      <li><svg class="tick" viewBox="0 0 12 12"><path d="M1 6.5l3 3L11 2" fill="none" stroke="#0f2a5c" stroke-width="2"/></svg>Professional investment management</li>
      <li><svg class="tick" viewBox="0 0 12 12"><path d="M1 6.5l3 3L11 2" fill="none" stroke="#0f2a5c" stroke-width="2"/></svg>Consolidate and simplify</li>
      <li><svg class="tick" viewBox="0 0 12 12"><path d="M1 6.5l3 3L11 2" fill="none" stroke="#0f2a5c" stroke-width="2"/></svg>Guaranteed lifetime income options</li>
      <li><svg class="tick" viewBox="0 0 12 12"><path d="M1 6.5l3 3L11 2" fill="none" stroke="#0f2a5c" stroke-width="2"/></svg>Help from a team of dedicated advisors</li>
    </ul>
  </div>

  <div class="cta">
    Make the most of your old 401k with a new<br>Rollover IRA, speak with a trusted advisor
    <div class="cta-phone">
      <svg width="14" height="14" viewBox="0 0 24 24"><path d="M6.6 10.8a15.1 15.1 0 006.6 6.6l2.2-2.2a1 1 0 011-.25 11.4 11.4 0 003.6.57 1 1 0 011 1V20a1 1 0 01-1 1A17 17 0 013 4a1 1 0 011-1h3.5a1 1 0 011 1 11.4 11.4 0 00.57 3.6 1 1 0 01-.25 1z" fill="#1a1a1a"/></svg>
      661-555-0142
    </div>
  </div>

  <p class="disclosure">Securities offered through Ember Ridge Securities, L.P. Member - NEVOC/TALQ | 4875 North Elm Rd, Ste 120, Lancaster, CA 93536 | 800.555.0173 | CA Ins. Lic. #0K48391, #0713948, #0K52806, #0619427</p>
</section>

</body>
</html>
```